Fenwick Salve by Tidy Owls: All Natural Lip Balm Co. Looking for New Label

Greetings, our company is called Tidy Owls and we are a start-up founded in early 2014. We make 100% All-Natural lip balm, called Fenwick Salve, in a variety of flavors and we are looking for a new label that incorporates part of our logo and highlights our product name and our lip balms flavor (see attached files). Our website is: fenwicksalve.example, and we are on Twitter: @TidyOwlsSalves, and Facebook: /TidyOwlsSalves. Our lip balms are made with beeswax, sweet almond oil, shea butter, coconut oil and other all natural oils and flavors.

The design should be clean, and communicate comfort, its "all-natural-ness", reliability, and fun. The colors we would like to have incorporated are burgundy, a deep, but not dark orange (see files, website, logo, graphics), some green and maybe gold/yellow. Given that the lip balm tubes are small (standard tubes), we would like to assure that the lip balm name, the flavor, and part of the logo- (perhaps the bee), are clearly visible and easily read. I am open to a variety of fonts, as long as they convey what I have stated above.

We want to use the label graphics and our logo for not only labeling our product, but also for use on our website, on banners, signs, retail boxes, letterhead, tee shirts, etc. If we like the design we are open to working with you again as our company is growing and we will be expanding our product line within the year to include hand and body balms, as well as other similar items and we will eventually have a few different product lines marketed at various age groups as well. Our lip balm is currently marketed to 14 to 40+ demographic, with the average age being roughly in the 15 to 24 range and our lip balm has been purchased by more women than men, though we market to both.

As far as software goes, I would like it to be in a format that is most popular- my old logo and graphics were made in Adobe Creative Suite 5.0, Adobe InDesign, and Adobe Illustrator, so the label should be made using this software (or a higher version). If I can have the label in a JPEG format also so I personally can add it to my website and social media that would be great.

I have a label redesign doc in an indd format but it was too large to upload. I believe this was the entire layout of our last label. If you need this, or anything else, please let me know as well as how I can send it to you.

We have applied to the popular TV show Crane Court and recently received a call back with interest from the producers; we are so excited and hope you are as well!

Thank you!
Rolf Dagestad
Owner
Tidy Owls Salves LLC
Rolf@TidyOwlsSalves.example

The Label dimensions are: 2.25 inches wide ---> by 2 inches long. Currently, there is a .75 inch area that is part of the label and is perforated, used as a safety seal. I may be changing the labels to a slightly different kind but the dimensions will be the same. The tubes we use are standard lip balm tubes with a net weight of .15 ounces ( the total length of the tube from the bottom turning piece to the top of the cap is just over 2.5 inches (this is NOT how large the label must be).We are discontinuing the 1 Hive, 2 Hive concepts ( for different consistencies of the balm) so that part of the label does not need to be included.Feel free to enhance and/or modify the logo to fit the design of the label.Thank you! Added Thursday, February 12, 2015

Requirements
Must have
• Label Dimensions:
• Length: 2.125" Height: 2.125"
• Top Margin: 1.025" Bottom Margin: 1.025"
• Left Margin: 0.9125" Right Margin: 0.9125"
• Horizontal Spacing: 0.15" Vertical Spacing: 0.15"
• Horizontal Pitch: 2.275" Vertical Pitch: 2.275"

```html
<!DOCTYPE html>
<html lang="en">
<head>
<meta charset="utf-8">
<title>Fenwick Salve – Beeswax Lip Balm Label</title>
<link href="https://fonts.googleapis.com/css2?family=Federo&family=Yanone+Kaffeesatz:wght@500&family=Roboto:wght@700&display=swap" rel="stylesheet">
<style>
  :root {
    --bg: #f1f1f1;
    --label-cream: #fdf7ee;
    --label-honey: #f6e6cf;
    --orange: #f0a129;
    --orange-deep: #e8951d;
    --burgundy: #8a1f2b;
    --white: #ffffff;
    --bee-gold: #f4b43c;
    --bee-green: #7fb88a;
  }
  html, body {
    margin: 0;
    padding: 0;
    width: 1200px;
    height: 1200px;
    overflow: hidden;
    background: var(--bg);
  }
  .canvas {
    position: relative;
    width: 1200px;
    height: 1200px;
  }
  .label {
    position: absolute;
    left: 120px;
    top: 505px;
    width: 830px;
    height: 300px;
    background: var(--label-cream);
    overflow: hidden;
  }
  .honeycomb-field {
    position: absolute;
    inset: 0 100px 0 0;
    background: linear-gradient(180deg, var(--label-cream) 0%, var(--label-honey) 60%, var(--label-cream) 100%);
  }
  .brand-mark {
    position: absolute;
    left: 140px;
    top: 25px;
    width: 110px;
    height: 110px;
    border-radius: 50%;
    background: var(--orange);
  }
  .brand-name {
    position: absolute;
    left: 30px;
    top: 172px;
    margin: 0;
    font-family: "Yanone Kaffeesatz", "Arial Narrow", sans-serif;
    font-weight: 500;
    font-size: 82px;
    line-height: 1;
    color: var(--orange);
    white-space: nowrap;
  }
  .mascot-art {
    position: absolute;
    left: 505px;
    top: 12px;
    width: 170px;
    height: 112px;
    border-radius: 10px;
    background: linear-gradient(135deg, var(--bee-gold) 0%, #f7cf7a 60%, var(--bee-green) 100%);
  }
  .maker-name {
    position: absolute;
    left: 462px;
    top: 136px;
    margin: 0;
    font-family: "Federo", sans-serif;
    font-size: 42px;
    line-height: 1;
    color: var(--burgundy);
    white-space: nowrap;
  }
  .maker-name .llc {
    font-size: 13px;
    vertical-align: top;
    margin-left: 2px;
  }
  .product-type {
    position: absolute;
    left: 440px;
    top: 203px;
    width: 255px;
    padding: 5px 0 4px;
    border-top: 2px solid var(--orange);
    border-bottom: 2px solid var(--orange);
    font-family: "Roboto", Arial, sans-serif;
    font-weight: 700;
    font-size: 21px;
    letter-spacing: 0.5px;
    text-align: center;
    color: var(--orange-deep);
  }
  .flavor-pill {
    position: absolute;
    left: 436px;
    top: 252px;
    width: 262px;
    height: 34px;
    border-radius: 17px;
    background: var(--orange);
    font-family: "Roboto", Arial, sans-serif;
    font-weight: 700;
    font-size: 18px;
    line-height: 34px;
    text-align: center;
    color: var(--white);
  }
  .side-band {
    position: absolute;
    right: 0;
    top: 0;
    width: 100px;
    height: 100%;
    background: var(--orange);
    overflow: hidden;
  }
  .side-band-name {
    position: absolute;
    left: 50%;
    top: 12px;
    transform-origin: 0 0;
    transform: rotate(90deg) translateY(-50%);
    margin: 0;
    font-family: "Yanone Kaffeesatz", "Arial Narrow", sans-serif;
    font-weight: 500;
    font-size: 56px;
    line-height: 1;
    color: var(--white);
    white-space: nowrap;
  }
</style>
</head>
<body>
  <div class="canvas">
    <div class="label">
      <div class="honeycomb-field" role="img" aria-label="Soft honeycomb pattern in cream and honey tones"></div>

      <div class="brand-mark"></div>
      <h1 class="brand-name">Fenwick Salve</h1>

      <div class="mascot-art" role="img" aria-label="Illustration of a smiling cartoon bee mascot with green wings"></div>
      <p class="maker-name">Tidy Owls<span class="llc">LLC</span></p>

      <div class="product-type">BEESWAX LIP BALM</div>
      <div class="flavor-pill">Brown Sugar Cookie</div>

      <div class="side-band">
        <p class="side-band-name">Fenwick Salve</p>
      </div>
    </div>
  </div>
</body>
</html>
```